Business card design for crowd sourced review site.

I need a business card magnet design for an online, crowd-sourced, restaurant review site strictly for Kosher restaurants.
It is similar to WanderNotes but catering to a very particular crowd.
The markets it will be distributed in are flooded with business card fridge magnets so this needs to be eye-catching and unique. The Business name is PlateRanker
The website isnt finished but you can see the basic setup here
http://dining.brevtalo.com/

The second image i included is another logo design I liked and was thinking about using and decided I will probably also make a SECOND custom cut business card in the shape of that icon. Bonus if you can throw that in also.

Target Market(s)

Jewish consumers aged 20-35

Industry/Entity Type

Business

Contact Information for Business Card

see description.
Design should not be too crowded and should in eye-catching. Will mainly be used as fridge magnets.

Requirements
Must have
• Website address. logo.
Nice to have
• tagline. (The Definitive guide to kosher dining for the Kosher consumer)
• Im not a professional but I personally think the color blue goes along with this concept. ill leave it to you to decide.
Should not have
• any religious symbols.

```html
<!DOCTYPE html>
<html lang="en">
<head>
<meta charset="utf-8">
<title>PlateRanker Business Card</title>
<link rel="stylesheet" href="https://fonts.googleapis.com/css2?family=Source+Sans+3:wght@400;600&display=swap">
<style>
  :root {
    --backdrop: #ecebe8;
    --kraft-light: #cdb186;
    --kraft-mid: #c4a679;
    --kraft-dark: #b8996b;
    --ink: #141210;
    --card-shadow: rgba(60, 45, 25, 0.25);
  }
  * { margin: 0; padding: 0; box-sizing: border-box; }
  html, body {
    width: 1200px;
    height: 900px;
    overflow: hidden;
    background: var(--backdrop);
    font-family: "Source Sans 3", "Myriad Pro", Arial, sans-serif;
    color: var(--ink);
  }
  .canvas {
    position: relative;
    width: 1200px;
    height: 900px;
  }
  .card {
    position: absolute;
    width: 556px;
    height: 342px;
    background: linear-gradient(135deg, var(--kraft-light) 0%, var(--kraft-mid) 50%, var(--kraft-dark) 100%);
    box-shadow: 0 6px 18px var(--card-shadow);
    text-align: center;
  }
  .card--contact { left: 238px; top: 62px; }
  .card--brand { left: 460px; top: 518px; }

  .contact-name {
    position: absolute;
    top: 100px;
    width: 100%;
    font-size: 19px;
    font-weight: 600;
    line-height: 24px;
  }
  .contact-role {
    position: absolute;
    top: 122px;
    width: 100%;
    font-size: 15px;
    line-height: 20px;
  }
  .contact-details {
    position: absolute;
    top: 176px;
    width: 100%;
    list-style: none;
    font-size: 15px;
    line-height: 20.5px;
  }

  .brand-lockup {
    position: absolute;
    top: 106px;
    left: 0;
    width: 100%;
    display: flex;
    justify-content: center;
    align-items: center;
    gap: 16px;
  }
  .brand-dot {
    width: 50px;
    height: 50px;
    border-radius: 50%;
    background: var(--ink);
  }
  .brand-name {
    font-size: 40px;
    font-weight: 600;
    line-height: 1;
    color: var(--ink);
  }
  .brand-tagline {
    position: absolute;
    top: 236px;
    width: 100%;
    font-size: 22px;
    line-height: 25px;
    letter-spacing: 0.2px;
    text-transform: uppercase;
  }
</style>
</head>
<body>
  <main class="canvas">
    <section class="card card--contact" aria-label="Card back with contact details">
      <p class="contact-name">Daniel Reed</p>
      <p class="contact-role">Director</p>
      <ul class="contact-details">
        <li>1234567890</li>
        <li>info@platemail.com</li>
        <li>wwww.dining.brevtalo.com</li>
      </ul>
    </section>

    <section class="card card--brand" aria-label="Card front with brand">
      <div class="brand-lockup">
        <span class="brand-dot" aria-hidden="true"></span>
        <span class="brand-name">PlateRanker</span>
      </div>
      <p class="brand-tagline">The definitive guide to kosher<br>dining for the kosher consumer</p>
    </section>
  </main>
</body>
</html>
```